Harold T. Wexley, MD

I would like to set up a web page for my new psychiatric practice. It should summarize my credentials and approach to care plus a patient portal to complete forms before appointments.
I am uploading a powerpoint with my contact information along with the color palette and format I would like to use. The email on the slide has not been reserved and I will need to reserve the domain as part of this process.

```html
<!DOCTYPE html>
<html lang="en">
<head>
<meta charset="utf-8">
<title>Harold T. Wexley, MD, Inc — Psychiatric Practice</title>
<link rel="stylesheet" href="https://fonts.googleapis.com/css2?family=Roboto:wght@300;400;500;700&family=Roboto+Condensed:wght@400&family=Open+Sans:ital,wght@0,400;0,600;1,400;1,600&display=swap">
<style>
:root{
  --blue:#1a7fd4;
  --blue-dark:#136bbd;
  --blue-band:#2b8ee0;
  --orange:#f26b3a;
  --star:#f5a623;
  --ink:#333;
  --muted:#666;
  --line:#e4e4e4;
  --card:#f7f6f2;
  --footer:#f2f2f2;
}
*{margin:0;padding:0;box-sizing:border-box}
html,body{width:1200px;height:2356px;overflow:hidden;background:#fff}
body{font-family:"Open Sans",sans-serif;color:var(--ink);position:relative}
.abs{position:absolute}

/* header */
.toll{left:99px;top:50px;display:flex;gap:10px;align-items:center}
.toll small{display:block;font-size:10px;color:var(--muted);letter-spacing:.3px}
.toll strong{display:block;font-family:"Roboto",sans-serif;font-weight:400;font-size:16px;color:#444}
.brand{left:0;width:1200px;top:20px;text-align:center}
.brand .mark{width:52px;height:52px;border:3px solid var(--orange);border-radius:50%;margin:0 auto 6px}
.brand-name{font-family:"Roboto Condensed",sans-serif;font-size:29px;color:var(--blue);font-weight:400}
.book{left:924px;top:46px;width:176px;height:38px;border-radius:19px;background:var(--blue);color:#fff;font-family:"Roboto",sans-serif;font-size:14px;display:flex;align-items:center;justify-content:center}

.nav{left:99px;top:127px;width:1002px;height:51px;border-top:1px solid var(--line);display:flex;font-family:"Roboto",sans-serif;font-size:13px;color:#333}
.nav a{color:inherit;text-decoration:none;display:flex;align-items:center;justify-content:center;border-right:1px solid var(--line);margin:8px 0;padding:0 36px}
.nav a:last-child{border-right:0}
.nav a.current{color:var(--blue);padding-left:0;position:relative}
.nav a.current::before{content:"";position:absolute;top:-9px;left:0;width:36px;height:2px;background:var(--blue)}

/* hero */
.hero{left:0;top:178px;width:1200px;height:564px;background:linear-gradient(100deg,#e9e2da 0%,#cfc3b6 30%,#b8aa9b 55%,#3b3c44 75%,#ccc2b8 100%)}
.hero h1{position:absolute;left:130px;top:158px;font-family:"Roboto",sans-serif;font-weight:700;font-size:56px;line-height:1.0;color:#fff;text-shadow:0 2px 6px rgba(0,0,0,.25)}
.hero p{position:absolute;left:134px;top:288px;width:370px;font-size:13px;line-height:23px;color:#fff}
.arrow{width:44px;height:44px;border:2px solid rgba(255,255,255,.85);border-radius:50%;top:402px}

/* service cards */
.cards{left:99px;top:676px;width:1002px;height:311px;display:flex;background:var(--card);border:1px solid var(--line)}
.card{flex:1;text-align:center;position:relative;border-right:2px solid #222}
.card:last-child{border-right:0}
.card .ic{width:112px;height:112px;border-radius:50%;background:var(--blue);border:5px solid #fff;box-shadow:0 1px 4px rgba(0,0,0,.2);margin:-44px auto 0;display:flex;align-items:center;justify-content:center}
.card h3{font-family:"Roboto",sans-serif;font-weight:300;font-size:21px;color:#444;margin-top:20px}
.card p{font-size:11.5px;line-height:20px;color:#666;width:285px;margin:12px auto 0}
.more{display:inline-flex;gap:8px;align-items:center;justify-content:center;width:122px;height:37px;border:1px solid var(--blue);border-radius:19px;color:var(--blue);font-family:"Roboto",sans-serif;font-size:11px;margin-top:24px}

/* welcome */
.welcome-photo{left:99px;top:1045px;width:251px;height:242px;background:linear-gradient(135deg,#d9d3cc,#b9c6d2 60%,#e8eef3)}
.welcome{left:382px;top:1043px;width:420px}
.welcome h2{font-family:"Roboto",sans-serif;font-weight:400;font-size:20px;color:#222}
.welcome h2 span{color:var(--blue)}
.welcome p{font-size:11.5px;line-height:20px;color:#555;margin-top:18px}
.welcome .info{display:inline-block;margin-top:22px;padding-top:12px;border-top:1px solid var(--line);font-family:"Roboto",sans-serif;font-size:13px;color:var(--blue);letter-spacing:.3px}
.dept-title{left:833px;top:1041px;font-family:"Roboto",sans-serif;font-size:14px;color:var(--blue)}
.dept{left:834px;top:1081px;width:267px;height:207px;border:1px solid var(--line);padding:22px 26px;list-style:none;font-family:"Roboto",sans-serif;font-size:14px;color:#444}
.dept li{height:31.5px;display:flex;align-items:center;gap:14px}
.dept li::before{content:"";width:10px;height:10px;border:1.5px solid #555;border-radius:50%}

/* practice band */
.band{left:0;top:1340px;width:1200px;height:429px;background:linear-gradient(180deg,#2d90e2,#1f7fd3)}
.band h2{position:absolute;top:50px;width:1200px;text-align:center;font-family:"Roboto",sans-serif;font-weight:400;font-size:26px;color:#fff}
.band h2::after{content:"";display:block;width:106px;height:1px;background:rgba(255,255,255,.8);margin:16px auto 0}
.tiles{position:absolute;left:99px;top:130px;display:flex;gap:15px}
.tile{width:239px;height:235px;position:relative}
.tile .cap{position:absolute;left:0;bottom:0;width:100%;height:55px;background:rgba(30,30,30,.75);color:#fff;padding:8px 12px}
.tile .cap b{display:block;font-family:"Roboto",sans-serif;font-weight:400;font-size:15px}
.tile .cap span{font-size:11px}

/* reviews */
.reviews-title{left:0;top:1820px;width:1200px;text-align:center;font-family:"Roboto",sans-serif;font-weight:300;font-size:33px;color:#333}
.reviews-title span{color:var(--blue)}
.review{top:1909px;width:470px;display:flex;gap:22px}
.avatar{width:119px;height:119px;border-radius:50%;flex:none;background:linear-gradient(160deg,#f1ece8,#cfd9e3)}
.review blockquote{font-style:italic;font-size:11.5px;line-height:21px;color:#444;padding-top:4px}
.review blockquote::before{content:"\201C";font-size:22px;color:#777;margin-right:4px}
.stars{color:var(--star);font-size:12px;margin-top:4px;letter-spacing:1px}
.stars i{color:#bbb;font-style:normal}
.reviewer{font-style:italic;font-weight:600;font-size:13px;color:var(--orange);margin-top:8px}

/* footer */
.footer{left:0;top:2086px;width:1200px;height:220px;background:var(--footer)}
.f-brand{position:absolute;left:97px;top:28px;width:200px;text-align:center}
.f-brand .mark{width:50px;height:50px;border:3px solid var(--orange);border-radius:50%;margin:0 auto 8px}
.f-brand .brand-name{font-size:21px}
.social{display:flex;gap:6px;justify-content:center;margin-top:14px}
.social i{width:22px;height:22px;border-radius:50%;background:#9aa6b2}
.f-col{position:absolute;top:38px}
.f-col h4{font-family:"Roboto",sans-serif;font-weight:400;font-size:15px;color:#222;margin-bottom:14px}
.f-col ul{list-style:none;font-size:11px;line-height:23px;color:#555}
.f-col p{font-size:11.5px;line-height:19px;color:#555}
.signup{display:flex;margin-top:18px}
.signup span{width:165px;height:40px;background:#fff;font-size:11px;display:flex;align-items:center;padding-left:13px;color:#444}
.signup b{width:98px;height:40px;background:var(--blue);color:#fff;font-family:"Roboto",sans-serif;font-weight:400;font-size:13px;display:flex;align-items:center;justify-content:center}
.c-row{display:flex;gap:16px;align-items:center;margin-top:12px;font-size:14px;color:#444}
.bottom{left:0;top:2306px;width:1200px;height:50px;background:var(--blue);color:#fff;font-size:11px;display:flex;align-items:center;justify-content:center}
</style>
</head>
<body>

<header>
  <div class="abs toll">
    <svg width="16" height="26" viewBox="0 0 16 26"><rect x="1" y="1" width="14" height="24" rx="2" fill="none" stroke="#1a7fd4" stroke-width="2"/><circle cx="8" cy="21" r="1.3" fill="#1a7fd4"/></svg>
    <div><small>CALL TOLL FREE</small><strong>08 5550 1234</strong></div>
  </div>
  <div class="abs brand">
    <div class="mark"></div>
    <div class="brand-name">Harold T. Wexley, MD, Inc</div>
  </div>
  <div class="abs book">BOOK APPOINMENT</div>
  <nav class="abs nav">
    <a class="current">HOME</a>
    <a>ABOUT HAROLD T</a>
    <a>OUR SERVICES</a>
    <a>CONSULTATION</a>
    <a>NEWS &amp; EVENTS</a>
    <a>CONTACT US</a>
  </nav>
</header>

<section class="abs hero" role="img" aria-label="Photo of a psychiatrist in a suit talking with a patient on a sofa">
  <h1>PSYCHIATRIC<br>PRACTICE</h1>
  <p>Nemo enim ipsam voluptatem quia voluptas sit aspernatur aut odit aut fugit, sed quia</p>
  <svg class="abs arrow" style="left:36px" viewBox="0 0 44 44"><path d="M25 14l-8 8 8 8" fill="none" stroke="#fff" stroke-width="2"/></svg>
  <svg class="abs arrow" style="left:1112px" viewBox="0 0 44 44"><path d="M19 14l8 8-8 8" fill="none" stroke="#fff" stroke-width="2"/></svg>
</section>

<section class="abs cards">
  <article class="card">
    <div class="ic"><svg width="52" height="44" viewBox="0 0 52 44" fill="#fff"><circle cx="16" cy="12" r="7"/><path d="M3 38c0-9 6-14 13-14s13 5 13 14z"/><circle cx="37" cy="10" r="6"/><path d="M27 30c1-7 5-11 10-11s11 4 11 11z"/></svg></div>
    <h3>Consultation</h3>
    <p>Lorem ipsum dolor sit amet, consectetur adipiscing elit, sed do eiusmod tempor incididunt ut labore et dolore magna aliqua. Ut enim ad minim veniam, quis nostrud exercitation ullamco laboris nisi</p>
    <span class="more">READ MORE <svg width="8" height="8" viewBox="0 0 8 8"><path d="M1 1l6 6M7 3v4H3" fill="none" stroke="#1a7fd4"/></svg></span>
  </article>
  <article class="card">
    <div class="ic"><svg width="46" height="46" viewBox="0 0 46 46" fill="#fff"><circle cx="23" cy="20" r="9"/><path d="M8 44c0-10 7-15 15-15s15 5 15 15z"/><path d="M14 4l3 5M23 1v6M32 4l-3 5" stroke="#fff" stroke-width="2"/></svg></div>
    <h3>Professional Issues</h3>
    <p>Lorem ipsum dolor sit amet, consectetur adipiscing elit, sed do eiusmod tempor incididunt ut labore et dolore magna aliqua. Ut enim ad minim veniam, quis nostrud exercitation ullamco laboris nisi</p>
    <span class="more">READ MORE <svg width="8" height="8" viewBox="0 0 8 8"><path d="M1 1l6 6M7 3v4H3" fill="none" stroke="#1a7fd4"/></svg></span>
  </article>
  <article class="card">
    <div class="ic"><svg width="44" height="46" viewBox="0 0 44 46" fill="#fff"><circle cx="22" cy="13" r="10"/><path d="M4 46c0-12 8-18 18-18s18 6 18 18z"/><circle cx="30" cy="38" r="3" fill="#1a7fd4"/></svg></div>
    <h3>Maintaining Your Practice</h3>
    <p>Lorem ipsum dolor sit amet, consectetur adipiscing elit, sed do eiusmod tempor incididunt ut labore et dolore magna aliqua. Ut enim ad minim veniam, quis nostrud exercitation ullamco laboris nisi</p>
    <span class="more">READ MORE <svg width="8" height="8" viewBox="0 0 8 8"><path d="M1 1l6 6M7 3v4H3" fill="none" stroke="#1a7fd4"/></svg></span>
  </article>
</section>

<div class="abs welcome-photo" role="img" aria-label="Photo of a smiling doctor in a white coat consulting with a patient"></div>
<section class="abs welcome">
  <h2>WELCOME TO <span>HAROLD T. WEXLEY, MD, INC</span></h2>
  <p>Lorem ipsum dolor sit amet, consectetur adipiscing elit, sed do eiusmod tempor incididunt ut labore et dolore magna aliqua. Ut enim ad minim veniam, quis nostrud exercitation&nbsp; Lorem ipsum dolor sit amet, consectetur adipiscing elit, sed do eiusmod tempor incididunt .</p>
  <p>Lorem ipsum dolor sit amet, consectetur adipiscing elit, sed do eiusmod tempor incididunt ut labore et dolore magna aliqua. Ut enim ad minim veniam, quis nostrud exercitation&nbsp; Lorem ipsum dolor sit amet,</p>
  <span class="info">MORE INFO ➜</span>
</section>
<h3 class="abs dept-title">DEPARTMENT OF PSYCHIATRIC</h3>
<ul class="abs dept">
  <li>Mission Statement</li>
  <li>Managed Care Issues</li>
  <li>Make An Appointment</li>
  <li>Establishing Your Own Practice</li>
  <li>Legal Issues</li>
</ul>

<section class="abs band">
  <h2>PSYCHIATRIC PRACTICE</h2>
  <div class="tiles">
    <div class="tile" role="img" aria-label="Photo of a distressed man with a counsellor" style="background:linear-gradient(135deg,#e9e7e2,#b9c0c8)"><div class="cap"><b>Nemo enim ipsam</b><span>Lorem ipsum dolor sit amet, consect</span></div></div>
    <div class="tile" role="img" aria-label="Photo of hands holding a brain scan tablet" style="background:linear-gradient(135deg,#cfe1ec,#7fa8c6)"><div class="cap"><b>Nemo enim ipsam</b><span>Lorem ipsum dolor sit amet, consect</span></div></div>
    <div class="tile" role="img" aria-label="Photo of a psychiatrist talking with a patient" style="background:linear-gradient(135deg,#e8e4df,#4a4b52)"><div class="cap"><b>Nemo enim ipsam</b><span>Lorem ipsum dolor sit amet, consect</span></div></div>
    <div class="tile" role="img" aria-label="Photo of a woman on a sofa during a therapy session" style="background:linear-gradient(135deg,#e2e4e6,#aeb4ba)"><div class="cap"><b>Nemo enim ipsam</b><span>Lorem ipsum dolor sit amet, consect</span></div></div>
  </div>
</section>

<h2 class="abs reviews-title">Customer <span>Reviews</span></h2>
<article class="abs review" style="left:99px">
  <div class="avatar" role="img" aria-label="Portrait photo of a female doctor"></div>
  <div>
    <blockquote>Lorem ipsum dolor sit amet, consectetur adipiscing elit, sed do eiusmod tempor incididunt ut labore et dolore magna aliqua. Ut enim ad minim veniam, quis nostrud</blockquote>
    <div class="stars">★★★<i>☆☆</i></div>
    <div class="reviewer">JOHN DOE</div>
  </div>
</article>
<article class="abs review" style="left:643px">
  <div class="avatar" role="img" aria-label="Portrait photo of a male doctor"></div>
  <div>
    <blockquote>Lorem ipsum dolor sit amet, consectetur adipiscing elit, sed do eiusmod tempor incididunt ut labore et dolore magna aliqua. Ut enim ad minim veniam, quis nostrud</blockquote>
    <div class="stars">★★★<i>☆☆</i></div>
    <div class="reviewer">JOHN DOE</div>
  </div>
</article>

<footer class="abs footer">
  <div class="f-brand">
    <div class="mark"></div>
    <div class="brand-name">Harold T. Wexley, MD, Inc</div>
    <div class="social"><i></i><i></i><i></i><i></i></div>
  </div>
  <div class="f-col" style="left:338px">
    <h4>INFORMATION</h4>
    <ul><li>Mission Statement</li><li>Psychiatric Practice</li><li>Make An Appointment</li><li>Services</li><li>Contact Us</li></ul>
  </div>
  <div class="f-col" style="left:571px;width:270px">
    <h4>SIGN UP FOR NEWSLETTER</h4>
    <p>Excepteur sint occaecat cupidatat non proident, sunt in culpa qui officia deserunt</p>
    <div class="signup"><span>Enter Name</span><b>SUBSCRIBE</b></div>
  </div>
  <div class="f-col" style="left:880px">
    <h4>CONTACT US</h4>
    <p>Harold T. Wexley, MD, Inc<br>PO BOX TBA, Millbrook</p>
    <div class="c-row" style="margin-top:18px"><svg width="18" height="18" viewBox="0 0 18 18"><path d="M4 1l3 4-2 2c1 2 3 4 5 5l2-2 4 3-2 3C8 16 2 10 1 4z" fill="none" stroke="#1a7fd4" stroke-width="1.4"/></svg>+1 03 5550 1299</div>
    <div class="c-row" style="font-size:12.5px"><svg width="18" height="14" viewBox="0 0 18 14"><rect x="1" y="1" width="16" height="12" fill="none" stroke="#1a7fd4" stroke-width="1.4"/><path d="M1 1l8 7 8-7" fill="none" stroke="#1a7fd4" stroke-width="1.4"/></svg>info@htwexleymd.com</div>
  </div>
</footer>
<div class="abs bottom">©2015 - 2016&nbsp; HAROLD T. WEXLEY, MD, INC., All Rights Reserved.</div>

</body>
</html>
```